Luxury Candle Startup Needs Modern Packaging Box & Matching Label Design

We are Wickhollow, a luxury candle company about to launch in Australia and we need a box packaging design that is modern, minimalist, and feminine. Our target audience are females, mostly mothers, within the age range of 25-45 who are looking for high quality, handmade luxurious products. Our company is going to have a large social media presence with new mothers as we are going to show our journey with starting a business whilst on maternity leave. We would like the arch shape incorporated into the box packaging as it is beautiful and symbolises moving into a new phase in life which really represents the brand. We would like for the packaging box to be a simple white box with a sleeve insert over the box with the design to make printing easier. Our colour inspiration are very earthy colours and would like the sleeve colour to be easily changed according to the scent. For example dusky rose coloured sleeve for rose patchouli and amber scent, light coffee coloured sleeve for coffee bean cacao scent etc. Please see uploaded files for inspiration, our logo, and the type of candle jars used.
The box dimensions are:
External Dimension: 95mmW x 95mmL x 116mmH
We look forward to seeing your amazing designs!

```html
<!DOCTYPE html>
<html lang="en">
<head>
<meta charset="UTF-8">
<title>Wickhollow – Rose Patchouli Box Sleeve</title>
<link rel="stylesheet" href="https://fonts.googleapis.com/css2?family=Cormorant+Garamond:wght@300&family=Josefin+Sans:wght@400;600&display=swap">
<style>
  :root {
    --backdrop: #f3f2ee;
    --box-white: #fbfbf9;
    --box-edge: #e6e5e0;
    --sleeve-base: #ebebe8;
    --arch-top: #f2d2bb;
    --arch-bottom: #dfb596;
    --wordmark: #c29b79;
    --gold: #a8783e;
    --ornament: #e8c4a6;
  }
  * { margin: 0; padding: 0; box-sizing: border-box; }
  html, body {
    width: 1200px;
    height: 1072px;
    overflow: hidden;
    background: var(--backdrop);
  }
  .canvas {
    position: relative;
    width: 1200px;
    height: 1072px;
  }
  .box-front {
    position: absolute;
    left: 320px;
    top: 194px;
    width: 560px;
    height: 684px;
    background: var(--box-white);
    border: 1px solid var(--box-edge);
  }
  .sleeve {
    position: absolute;
    left: 112px;
    top: 0;
    width: 336px;
    height: 100%;
    background: var(--sleeve-base);
  }
  .arch {
    position: absolute;
    left: 0;
    top: 0;
    width: 336px;
    height: 540px;
    background: linear-gradient(to bottom, var(--arch-top) 0%, var(--arch-bottom) 18%, var(--arch-bottom) 100%);
    border-radius: 0 0 168px 168px;
  }
  .wordmark {
    position: absolute;
    left: 50%;
    top: 232px;
    transform: translate(-50%, -50%) rotate(90deg);
    font-family: "Cormorant Garamond", serif;
    font-weight: 300;
    font-size: 40px;
    letter-spacing: 4px;
    text-transform: uppercase;
    color: var(--wordmark);
    white-space: nowrap;
  }
  .scent-name, .tagline, .origin {
    position: absolute;
    left: 0;
    width: 100%;
    text-align: center;
    font-family: "Josefin Sans", sans-serif;
    color: var(--gold);
    text-transform: uppercase;
  }
  .scent-name {
    top: 436px;
    font-size: 16px;
    font-weight: 600;
    letter-spacing: 2px;
  }
  .tagline {
    top: 464px;
    font-size: 11px;
    font-weight: 400;
    letter-spacing: 1.6px;
  }
  .origin {
    top: 484px;
    font-size: 9px;
    font-weight: 400;
    letter-spacing: 1.6px;
  }
  .ornament {
    position: absolute;
    left: 22px;
    top: 584px;
    width: 292px;
    height: 88px;
  }
</style>
</head>
<body>
  <div class="canvas">
    <div class="box-front">
      <div class="sleeve">
        <div class="arch">
          <div class="wordmark">Wickhollow</div>
          <div class="scent-name">Rose Patchouli</div>
          <div class="tagline">Luxury Fragrance</div>
          <div class="origin">Australia</div>
        </div>
        <svg class="ornament" viewBox="0 0 292 88" role="img" aria-label="Decorative floral ornament with leaves and small blossoms">
          <rect x="0" y="0" width="292" height="88" rx="10" fill="var(--ornament)" opacity="0.55"/>
        </svg>
      </div>
    </div>
  </div>
</body>
</html>
```